"Maple Nook" needs a A5 flyer for its "Art Contest"

Maple Nook needs a double sided A5 Flyer that illustrates in a child-friendly look the following competition:

Search for the up and coming Bright Sprout. The aim of our Bright Sprout is to allow our children to explore the artist within them and motivate them to express their talents through the fine art of drawing and painting.

Description: I have an art school, "Maple Nook", where children of 3-5 years old attend and learn how to paint and draw. We are making a competition where each child gets to draw a picture which we will upload to Chirpwall and parents will vote for best picture. We need to distribute to the parents a flyer with following content.

Competition Name: Bright Sprout

Front Side (content):
No major text on the front. Only the Logo and messages grabbing the readers attention such as "Who will be our next Artist?", "Vote for your Child", "Like Us on our Chirpwall Page".

Back Side (content):
Back side content is divided into 3 sections:

Section1:
How it Works?
Every child of every class will participate. Photos will be grouped by class.
There will be a Bright Sprout for each class, and there will be a Bright Sprout for the school.

Section2:
How to Participate?
In our search for ‘Bright Sprout’, we will select one piece of artwork from each child in the school, photograph it and upload it to our Chirpwall page.
Vote for your favourite painting by following the steps below:
1- From your chirpwall account go to www.chirpwall.example/Maple Nook
and “Like Us” to become a fan
2- Click on the“Bright Sprout” from the application menu
3- Browse through the different classes and vote for each picture you like
4- Invite your friends to vote for the picture you like to increase the chances of winning
The artist of the painting with most “Likes” will be crowned ‘Bright Sprout’.

Section3:
Note (in the footer):
Please note that the winner’s photo will be displayed in our “Bright Sprout” Frame on our Chirpwall landing page. If you do not want your child’s photograph to be posted on our Chirpwall page in this manner, please let us know by sending an e-mail.
, Maple Nook needs a double sided A5 Flyer that illustrates in a child-friendly look the following competition:

Front Side (content):

Back Side (content):

Section1:
How it Works?

Section2:
How to Participate?

Section3:
Note (in the footer):

Reason: To give more time for improvements on submitted designs and if possible some additional submissions.

Target Market(s)

Parents of the children attending at our school, Parents of the children attending at our school

Industry/Entity Type

Painting

Requirements
Must have
• Colors used in the design should be strict to our logo colors. We have 4 colors in our logo feel free to use one or all of them through out the design:
#6CB53C
#DB2718
#5D9DD5
#F4D602

The elements in our logo are playful and hand drawn and written, so the flyer design should reflect the hand made style rather than solid elements and objects., Colors used in the design should be strict to our logo colors. We have 4 colors in our logo feel free to use one or all of them through out the design:
#6CB53C
#DB2718
#5D9DD5
#F4D602

The elements in our logo are playful and hand drawn and written, so the flyer design should reflect the hand made style rather than solid elements and objects.
Should not have
• Images of real children., Images of real children.

```html
<!DOCTYPE html>
<html lang="en">
<head>
<meta charset="utf-8">
<title>Maple Nook – Bright Sprout Art Contest Flyer</title>
<link rel="stylesheet" href="https://fonts.googleapis.com/css2?family=Cinzel:wght@900&family=Open+Sans:wght@600;700&family=Oswald:wght@600&family=Gochi+Hand&family=Mali:wght@500&display=swap">
<style>
  :root{
    --green:#6CB53C;
    --red:#DB2718;
    --blue:#5D9DD5;
    --yellow:#F4D602;
    --cyan:#2aa7df;
    --navy:#2b2a7d;
    --pink:#e8508a;
    --grey:#c9c9d2;
    --paper:#fbfcf7;
    --mint:#eef3e2;
    --confetti:#f0e8ef;
  }
  *{margin:0;padding:0;box-sizing:border-box}
  html,body{width:1200px;height:840px;overflow:hidden;background:#fff}
  .flyer{position:relative;width:1200px;height:840px;background:#fff}

  /* ---------- front side ---------- */
  .front{
    position:absolute;left:0;top:0;width:606px;height:840px;
    background:linear-gradient(180deg,#f7f9f0 0%,var(--mint) 55%,#f3f6ec 100%);
  }
  .confetti-frame{
    position:absolute;inset:0;border:14px solid var(--confetti);pointer-events:none;
  }
  .brand{
    position:absolute;left:0;width:100%;top:48px;text-align:center;
    font-family:"Mali",cursive;font-weight:500;font-size:78px;color:var(--grey);letter-spacing:4px;
  }
  .headline-art{
    position:absolute;left:70px;top:205px;width:420px;height:245px;border-radius:14px;
    background:linear-gradient(160deg,#f6d9d6 0%,#f7e9c9 55%,#f1dcd9 100%);
  }
  .vote-box{
    position:absolute;left:38px;top:520px;width:530px;height:92px;
    border:5px dotted var(--red);padding:4px;
  }
  .vote-box-inner{
    width:100%;height:100%;border:4px dotted var(--red);
    display:flex;align-items:center;justify-content:center;gap:8px;
  }
  .vote-text{
    font-family:"Mali",cursive;font-weight:500;font-size:34px;color:#e4662a;letter-spacing:1px;
  }
  .vote-figure{width:34px;height:40px;background:#ee8a5a;border-radius:6px}
  .like-us{
    position:absolute;right:38px;top:686px;
    font-family:"Oswald",sans-serif;font-weight:600;font-size:34px;letter-spacing:.3px;
    background:linear-gradient(180deg,#7fb6e6 0%,var(--blue) 45%,#2f63a8 100%);
    -webkit-background-clip:text;background-clip:text;color:transparent;
  }
  .social-line{position:absolute;left:415px;top:744px;display:flex;align-items:center;gap:8px}
  .social-square{width:26px;height:26px;background:#3b5a98;border-radius:4px}
  .social-name{font-family:"Open Sans",sans-serif;font-weight:700;font-size:13px;color:#3b5a98}
  .social-rules{width:120px;height:10px;border-top:1px solid #999;border-bottom:1px solid #999}

  /* ---------- back side ---------- */
  .back{position:absolute;left:606px;top:0;width:594px;height:840px;background:#fff}
  .back-edge{position:absolute;left:0;top:0;width:12px;height:840px;background:var(--confetti)}
  .section-title{
    position:absolute;font-family:"Cinzel",serif;font-weight:900;color:var(--navy);
    font-size:37px;line-height:1;letter-spacing:.5px;
  }
  .title-works{left:28px;top:30px}
  .title-participate{left:28px;top:200px}
  .info-box{
    position:absolute;font-family:"Open Sans",sans-serif;font-weight:700;color:var(--cyan);
    font-size:15.6px;line-height:21px;
    border:5px dashed var(--cyan);outline:3px dotted var(--pink);outline-offset:4px;
    padding:4px 8px;
  }
  .box-works{left:38px;top:78px;width:418px;height:104px}
  .box-participate{left:38px;top:249px;width:508px;height:392px}
  .note-tag{
    position:absolute;left:254px;top:656px;padding:0 10px;background:var(--yellow);
    font-family:"Oswald",sans-serif;font-weight:600;font-size:22px;color:var(--red);line-height:30px;
  }
  .note-box{
    position:absolute;left:26px;top:692px;width:538px;height:118px;
    border:8px dotted #d8d81a;padding:6px;
  }
  .note-inner{
    width:100%;height:100%;border:2px dotted var(--red);padding:8px 10px;
    font-family:"Open Sans",sans-serif;font-weight:700;font-size:12.6px;line-height:18px;color:var(--red);
  }
</style>
</head>
<body>
<main class="flyer">

  <section class="front">
    <div class="confetti-frame" role="img" aria-label="Border of scattered multicoloured confetti dots"></div>
    <div class="brand">Maple Nook</div>
    <div class="headline-art" role="img" aria-label="Hand-lettered headline in red and orange: Who will be our next artist? with a drawn arrow and a yellow crown"></div>
    <div class="vote-box">
      <div class="vote-box-inner">
        <span class="vote-text">VOTE FOR YOUR CHILD</span>
        <span class="vote-figure" role="img" aria-label="Small drawn parent and child figures"></span>
      </div>
    </div>
    <p class="like-us">Like Us on our Chirpwall Page</p>
    <div class="social-line">
      <span class="social-square"></span>
      <span class="social-name">Chirpwall</span>
      <span class="social-rules"></span>
    </div>
  </section>

  <section class="back">
    <div class="back-edge" role="img" aria-label="Strip of scattered confetti dots"></div>

    <h2 class="section-title title-works">How it Works?</h2>
    <div class="info-box box-works">
      Every child of every class will participate.<br>
      Photos will be grouped by class.<br>
      There will be a Bright Sprout for each class,<br>
      and there will be a Bright Sprout for the school.
    </div>

    <h2 class="section-title title-participate">How to Participate?</h2>
    <div class="info-box box-participate">
      In our search for ‘Bright Sprout’, we will select one<br>
      piece of artwork from each child in the school,<br>
      photograph it and upload it to our Chirpwall page.<br>
      Vote for your favourite painting by following<br>
      the steps below:<br>
      1- From your chirpwall account go to<br>
      www.chirpwall.example/Maple Nook<br>
      and “Like Us” to become a fan<br>
      2- Click on the“Bright Sprout” from the application menu<br>
      3- Browse through the different classes and vote for<br>
      each picture you like<br>
      4- Invite your friends to vote for the picture you like to<br>
      increase the chances<br>
      of winning.<br>
      The artist of the painting with most “Likes”<br>
      will be crowned ‘Bright Sprout’.
    </div>

    <div class="note-tag">Note</div>
    <div class="note-box">
      <div class="note-inner">
        Please note that the winner’s photo will be displayed in our<br>
        “Bright Sprout” Frame on our Chirpwall landing page. If you do not want<br>
        your child’s photograph to be posted on our Chirpwall page<br>
        in this manner, please let us know by sending an e-mail.
      </div>
    </div>
  </section>

</main>
</body>
</html>
```